Kestrel Mobile Wellness Co

I am a Physical Therapist. I want to go to peoples homes and give them quality one on one care for their back/thoracic/neck pain. I will give them spinal mobilizations, massage and exercise. I will do all of this in the comfort of their homes. I will bring my massage table with me so I can work on their back and neck. Fee for service. Accept check and credit cards. I am an orthopaedic specialist and a Spine specialist. I will come to your door so you don't have to come to me.

working class and upper class

Massage

• Something to let the people know they will be treated special. They will get better care with me than if they were in an outpatient setting.

```html
<!DOCTYPE html>
<html lang="en">
<head>
<meta charset="utf-8">
<title>Kestrel Mobile Wellness Co – Postcard</title>
<link href="https://fonts.googleapis.com/css2?family=Jost:wght@400;500;600&family=Questrial&family=Lobster+Two:ital,wght@1,700&display=swap" rel="stylesheet">
<style>
  :root{
    --page:#2b3033;
    --blue:#2a64b4;
    --blue-deep:#123a8c;
    --blue-mid:#1d4fa6;
    --sky:#e4f0fb;
    --gold:#b08a3e;
    --yellow:#f8bd4f;
    --ink:#1b1b1b;
    --line:#4d7fc4;
    --white:#ffffff;
  }
  *{box-sizing:border-box;margin:0;padding:0}
  html,body{width:1200px;height:930px;overflow:hidden}
  body{background:var(--page);position:relative;font-family:"Questrial",sans-serif}

  .card{position:absolute;top:275px;width:540px;height:380px;overflow:hidden;box-shadow:0 8px 24px rgba(0,0,0,.45)}
  .card--front{left:40px;background:linear-gradient(90deg,var(--white) 30%,var(--sky))}
  .card--back{left:620px;background:var(--white)}

  .figure-panel{position:absolute;left:0;top:0;width:172px;height:300px;
    background:linear-gradient(160deg,var(--blue-mid),var(--blue-deep));
    border-top-right-radius:60px 140px}

  .title{position:absolute;font-family:"Jost",sans-serif;font-weight:500;color:var(--blue);font-size:34px;letter-spacing:.3px;line-height:1;white-space:nowrap}
  .subtitle{position:absolute;font-family:"Questrial",sans-serif;color:var(--gold);font-size:19px;line-height:1;white-space:nowrap}
  .card--front .title{left:188px;top:26px}
  .card--front .subtitle{left:200px;top:66px}

  .script{font-family:"Lobster Two",cursive;font-style:italic;font-weight:700;color:var(--gold)}
  .offer{position:absolute;left:196px;width:334px;text-align:center;color:var(--blue);white-space:nowrap}
  .offer .script{display:block;font-size:18px}
  .offer p{font-size:16px;margin-top:2px}
  .offer--focus{top:100px}
  .offer--services{top:158px}

  .promise{position:absolute;left:210px;top:218px;width:310px;border-top:1.5px solid var(--line);border-bottom:1.5px solid var(--line);
    padding:6px 4px;text-align:center;font-size:11.5px;color:var(--gold);line-height:1.35}
  .payment{position:absolute;right:20px;top:272px;font-size:15px;color:var(--ink);white-space:nowrap}

  .band{position:absolute;left:0;width:100%;background:var(--yellow);white-space:nowrap}
  .band--front{bottom:0;height:80px;display:flex;align-items:center;padding-left:30px;
    font-family:"Jost",sans-serif;color:var(--blue);font-size:30px}
  .band--front strong{font-weight:600;margin-right:8px}

  .card--back .title{left:22px;top:30px}
  .card--back .subtitle{left:34px;top:68px}
  .name-strip{position:absolute;left:0;top:92px;width:370px;height:34px;background:var(--yellow);white-space:nowrap;
    font-family:"Jost",sans-serif;font-weight:600;color:var(--white);font-size:21px;display:flex;align-items:center;padding-left:30px}
  .postage{position:absolute;right:22px;top:18px;width:112px;height:104px;border:2px solid var(--blue);
    color:var(--blue);font-size:14px;text-align:center;padding-top:18px;line-height:1.2}
  .address{position:absolute;left:280px;top:160px;width:238px}
  .address .to{font-size:13px;color:var(--ink);position:absolute;left:0;top:-2px}
  .address .rule{height:1.5px;background:var(--line);margin-left:22px;margin-bottom:34px}
  .ghost-figure{position:absolute;left:60px;top:150px;width:150px;height:140px;
    background:linear-gradient(180deg,rgba(190,200,225,.15),rgba(170,180,215,.4));border-radius:60px 60px 0 0}
  .band--back{bottom:0;height:86px;display:flex;align-items:center;justify-content:center;gap:10px;
    font-size:20px;color:var(--ink)}
  .band--back .script{color:var(--ink);font-size:17px}
</style>
</head>
<body>

<section class="card card--front">
  <div class="figure-panel" role="img" aria-label="Silhouette of a woman's back with the spine highlighted"></div>
  <h1 class="title">PHYSICAL THERAPIST</h1>
  <p class="subtitle">Orthopaedic and Spine Specialist</p>
  <div class="offer offer--focus">
    <span class="script">Specialist for</span>
    <p>Back • Thoracic • Neck pain</p>
  </div>
  <div class="offer offer--services">
    <span class="script">Services</span>
    <p>Spinal Mobilizations • Massage • Exercise</p>
  </div>
  <p class="promise">I will come to your door so you don't have to come to me. Massage Table Available</p>
  <p class="payment">Accept Check and Credit Cards</p>
  <div class="band band--front"><strong>KESTREL MOBILE</strong> Wellness Co</div>
</section>

<section class="card card--back">
  <h2 class="title">PHYSICAL THERAPIST</h2>
  <p class="subtitle">Orthopaedic and Spine Specialist</p>
  <div class="name-strip">KESTREL MOBILE WELLNESS CO</div>
  <div class="postage">Postage<br>Area</div>
  <div class="ghost-figure" role="img" aria-label="Faint outline of a woman's back with spine"></div>
  <div class="address">
    <span class="to">To</span>
    <div class="rule"></div>
    <div class="rule"></div>
    <div class="rule"></div>
    <div class="rule"></div>
  </div>
  <div class="band band--back"><span class="script">Specialist for</span> Back • Thoracic • Neck pain</div>
</section>

</body>
</html>
```